Update Letterhead for Harbor Vale Advisors

We need a modernized and updated letterhea. We DO NOT want to change fonts, we want incorporate the logo and words better and make a sleeker and elegant logo catering to wealthy clients. Harbor is a wealth management firm catering to business owners, physicians, and high net wort clientele. Our letterhead should have strength and elegance and cater to that market. Guaranteed payment.

Requirements
Must have
• PLEASE NOTE THAT THE LOGO USED IN THE ORIGINAL DESIGNS ARE INCORRECT! Please update to the new logo!
• We also changed our color scheme to grey and gold and black. Please refer to website www.harborva-example.com to see what I mean as we want to update to that rather than the dark blue. (Most likely grey and gold)

```html
<!DOCTYPE html>
<html lang="en">
<head>
<meta charset="utf-8">
<title>Harbor Vale Advisors Letterhead</title>
<link rel="stylesheet" href="https://fonts.googleapis.com/css2?family=Cinzel:wght@700&family=Tinos:wght@400;700&family=Josefin+Sans:wght@400;600&display=swap">
<style>
:root{
  --gold:#c9a355;
  --charcoal:#353535;
  --ink:#222;
  --paper:#fff;
  --backdrop:#e4e4e2;
  --watermark:#f3f3f3;
  --badge:#d8d8d8;
}
*{margin:0;padding:0;box-sizing:border-box}
html,body{width:1200px;height:1200px;overflow:hidden;background:var(--backdrop)}
.letterhead{
  position:absolute;left:170px;top:44px;width:1073px;height:1389px;
  background:var(--paper);transform:scale(.8);transform-origin:0 0;
  font-family:"Tinos","Times New Roman",serif;color:var(--ink);overflow:hidden;
}
.brand{position:absolute;left:35px;top:38px;display:flex;align-items:center;gap:12px}
.brand-dot{width:94px;height:94px;border-radius:50%;background:var(--gold);flex:none}
.brand-name{font-family:"Cinzel",serif;font-weight:700;color:var(--gold);line-height:1}
.brand-name .line-one{display:block;font-size:46px;letter-spacing:.5px}
.brand-name .line-two{display:block;font-size:46px;letter-spacing:.5px;margin-top:6px}
.side-band{position:absolute;right:0;top:0;width:39px;height:1128px;background:var(--gold)}
.band-icons{position:absolute;right:0;top:0;width:39px;height:220px}
.band-icons svg{position:absolute;left:13px;width:12px;height:12px}
.sender{position:absolute;right:44px;top:33px;text-align:right;font-size:13px;line-height:17.5px;white-space:nowrap}
.sender-name{color:var(--gold);font-weight:700;font-size:20px;line-height:24px}
.sender-title{font-weight:700;font-size:13.5px}
.office{margin-top:13px}
.office-label{color:var(--gold);font-weight:700;font-size:15px;line-height:17px}
.watermark{position:absolute;left:261px;top:419px;width:551px;height:551px;border-radius:50%;background:var(--watermark)}
.footer-bar{position:absolute;left:0;top:1234px;width:1073px;height:80px}
.mission{position:absolute;left:45px;top:1241px;font-family:"Josefin Sans",sans-serif;color:#fff;white-space:nowrap}
.mission h2{color:var(--gold);font-weight:400;font-variant:small-caps;font-size:23px;line-height:24px}
.mission p{font-size:14.5px;line-height:19px;text-transform:uppercase;margin-top:8px}
.badges{position:absolute;left:747px;top:1203px;width:305px;height:57px;display:flex;justify-content:space-between;align-items:flex-end}
.badge{background:var(--badge)}
.badge.round{width:60px;height:50px;border-radius:50%}
.badge.tri{width:60px;height:50px;clip-path:polygon(50% 0,100% 100%,0 100%)}
.badge.ring{width:48px;height:50px;border-radius:50%;background:none;border:6px solid var(--badge)}
.badge.key{width:24px;height:56px;border-radius:4px}
.disclaimer{position:absolute;left:45px;top:1322px;font-size:12.6px;line-height:17px;white-space:nowrap}
</style>
</head>
<body>
<div class="letterhead">
  <div class="brand">
    <div class="brand-dot"></div>
    <div class="brand-name"><span class="line-one">HARBOR VALE</span><span class="line-two">ADVISORS</span></div>
  </div>

  <div class="side-band"></div>
  <div class="band-icons" aria-hidden="true">
    <svg style="top:77px" viewBox="0 0 12 12"><path d="M2 1h3l1 3-2 1a7 7 0 0 0 3 3l1-2 3 1v3c-6 0-9-3-9-9z" fill="#fff"/></svg>
    <svg style="top:94px" viewBox="0 0 12 12"><rect x="1" y="2.5" width="10" height="7" fill="none" stroke="#fff"/><path d="M1 2.5l5 4 5-4" fill="none" stroke="#fff"/></svg>
    <svg style="top:111px" viewBox="0 0 12 12"><circle cx="6" cy="6" r="4.5" fill="none" stroke="#fff"/><path d="M1.5 6h9M6 1.5v9" stroke="#fff"/></svg>
    <svg style="top:140px" viewBox="0 0 12 12"><path d="M6 11S2 7 2 4.5a4 4 0 0 1 8 0C10 7 6 11 6 11z" fill="none" stroke="#fff" stroke-width="1.3"/><circle cx="6" cy="4.5" r="1.3" fill="#fff"/></svg>
    <svg style="top:180px" viewBox="0 0 12 12"><path d="M6 11S2 7 2 4.5a4 4 0 0 1 8 0C10 7 6 11 6 11z" fill="none" stroke="#fff" stroke-width="1.3"/><circle cx="6" cy="4.5" r="1.3" fill="#fff"/></svg>
  </div>

  <div class="sender">
    <div class="sender-name">Marian Hale Donovan, HVP, MFW , AQE</div>
    <div class="sender-title">PRESIDENT &amp; FINANCIAL ADVISOR</div>
    <div>555.010.4300</div>
    <div>mdonovan@harborva-example.com</div>
    <div>www.harborva-example.com</div>
    <div class="office">
      <div class="office-label">Downtown Office</div>
      <div>210 North Alder, Suite 1100 Ridgeport, TX 70001</div>
    </div>
    <div class="office">
      <div class="office-label">Westside Office</div>
      <div>4820 Lakeview Drive, Suite E1 Ridgeport, TX 70022</div>
    </div>
  </div>

  <div class="watermark" aria-hidden="true"></div>

  <div class="badges" aria-hidden="true">
    <div class="badge round"></div>
    <div class="badge tri"></div>
    <div class="badge ring"></div>
    <div class="badge key"></div>
  </div>

  <svg class="footer-bar" viewBox="0 0 1073 80" aria-hidden="true">
    <polygon points="0,0 672,0 722,46 1073,46 1073,80 0,80" fill="var(--charcoal)"/>
    <polygon points="718,35 1073,35 1073,43 727,43" fill="var(--gold)"/>
  </svg>

  <div class="mission">
    <h2>Our Mission Statement</h2>
    <p>“We empower our clients to realize financial independence by securing<br>today, tomorrow and the future. One family, one solution, and one legacy at a time.”</p>
  </div>

  <p class="disclaimer">*Marian Hale Donovan, HVP , a Financial Adviser offering investment advisory services through Summit Crest LLC, a Registered Investment Adviser. Registered Representative<br>offering securities through Northline Securities LLC, Member FSRA/SIPX, a Licensed Insurance Agency, 210 N. Alder Suite 1100, Ridgeport, TX 70001. 555-010-3200.<br>Member Agent, The Keystone Circle®, a service of Meridian Life Insurance Company. Harbor Vale Advisors is not owned or operated by Northline Securities LLC or its affiliates.</p>
</div>
</body>
</html>
```